Stationery Design Project - KLVA Partners

Business Cards
Size: 90mm x 55mm
Letterhead
Size: A4 - 210mm x 297mm
With Compliments Slip
Size: DL - 210mm x 99mm
Presentation Folder
Size: A4

KLVA Partners
website: www.klvapartners.com.au (Under construction)
Offices: *Perth *Brisbane * Seoul

A company that supply Safety consultantcy services

Industry/Entity Type

Business

```html
<!DOCTYPE html>
<html lang="en">
<head>
<meta charset="utf-8">
<title>KLVA Partners – Business Card</title>
<link href="https://fonts.googleapis.com/css2?family=Source+Sans+3:wght@300;400;600&display=swap" rel="stylesheet">
<style>
  :root {
    --page: #eeeeee;
    --card: #ffffff;
    --blue-deep: #0b3d84;
    --blue-mid: #0d5aa7;
    --blue-light: #1a7cc7;
    --blue-text: #1b4f9c;
    --steel: #6d6e71;
    --steel-light: #b9bcc2;
    --white: #ffffff;
  }
  * { margin: 0; padding: 0; box-sizing: border-box; }
  html, body { width: 1200px; height: 1040px; overflow: hidden; }
  body {
    background: var(--page);
    font-family: "Source Sans 3", "Myriad Pro", Arial, sans-serif;
    position: relative;
  }
  .card {
    position: absolute;
    left: 220px;
    width: 760px;
    height: 464px;
    background: var(--card);
    box-shadow: 0 6px 18px rgba(0,0,0,0.12);
    overflow: hidden;
  }
  .card--front { top: 36px; }
  .card--back { top: 540px; }

  /* Front */
  .brand-graphic {
    position: absolute; left: 0; top: 0; width: 200px; height: 150px;
    background: linear-gradient(135deg, var(--steel-light) 0%, #8fa3b8 45%, #3fa9e0 100%);
    clip-path: polygon(0 0, 100% 0, 100% 70%, 78% 100%, 0 100%);
  }
  .offices {
    position: absolute; left: 22px; top: 160px;
    font-size: 15px; font-weight: 600; color: var(--blue-text); letter-spacing: 0.3px;
  }
  .divider-vertical {
    position: absolute; left: 206px; top: 150px; width: 2px; height: 266px;
    background: var(--blue-mid);
  }
  .wordmark {
    position: absolute; left: 260px; top: 150px;
    display: flex; align-items: center; gap: 22px;
  }
  .wordmark__square { width: 62px; height: 62px; background: var(--steel); }
  .wordmark__name {
    font-size: 58px; font-weight: 300; color: var(--blue-text); letter-spacing: 1px;
  }
  .contact-band {
    position: absolute; left: 208px; top: 250px; width: 530px; height: 166px;
  }
  .contact-band > svg { position: absolute; inset: 0; }
  .contact-band__body {
    position: absolute; left: 42px; top: 12px; right: 22px; color: var(--white);
  }
  .person { font-size: 21px; font-weight: 400; }
  .person__title { font-size: 16px; margin-left: 14px; padding-left: 14px; border-left: 1px solid var(--white); }
  .address { font-size: 16px; margin-top: 6px; padding-bottom: 8px; border-bottom: 1px solid rgba(255,255,255,0.8); }
  .contact-grid {
    display: grid; grid-template-columns: 150px 1fr; row-gap: 4px; margin-top: 8px; font-size: 16px;
  }
  .contact-item { display: flex; align-items: center; gap: 8px; }
  .contact-item svg { width: 14px; height: 14px; flex: none; }

  /* Back */
  .back-panel {
    position: absolute; left: 22px; top: 22px; width: 716px; height: 420px;
    background: radial-gradient(ellipse at 55% 20%, var(--blue-light) 0%, var(--blue-mid) 45%, var(--blue-deep) 100%);
    clip-path: polygon(40px 0, 100% 0, 100% calc(100% - 40px), calc(100% - 40px) 100%, 0 100%, 0 40px);
  }
  .corner { position: absolute; width: 40px; height: 40px; background: var(--steel); }
  .corner--tl { left: 22px; top: 22px; clip-path: polygon(0 0, 100% 0, 0 100%); }
  .corner--br { right: 22px; bottom: 22px; clip-path: polygon(100% 0, 100% 100%, 0 100%); }
  .back-content {
    position: absolute; left: 22px; top: 22px; width: 716px; height: 420px;
    display: flex; flex-direction: column; align-items: center; justify-content: center;
    color: var(--white); text-align: center;
  }
  .back-name { display: flex; align-items: center; gap: 14px; font-size: 34px; font-weight: 300; margin-bottom: 22px; }
  .back-name__square { width: 38px; height: 38px; background: var(--steel-light); }
  .tagline { font-size: 21px; font-weight: 400; }
  .website { font-size: 21px; font-weight: 400; }
</style>
</head>
<body>

<section class="card card--front" aria-label="Business card front">
  <div class="brand-graphic" role="img" aria-label="Brand graphic in steel grey and bright blue"></div>
  <p class="offices">Darwin | Hobart | Osaka</p>
  <div class="divider-vertical"></div>

  <div class="wordmark">
    <span class="wordmark__square"></span>
    <span class="wordmark__name">KLVA Partners</span>
  </div>

  <div class="contact-band">
    <svg width="530" height="166" viewBox="0 0 530 166" aria-hidden="true">
      <defs>
        <linearGradient id="bandFill" x1="0" y1="0" x2="1" y2="0">
          <stop offset="0" stop-color="#0b3d84"/>
          <stop offset="1" stop-color="#1a7cc7"/>
        </linearGradient>
      </defs>
      <polygon points="28,0 530,0 530,138 502,166 0,166 0,28" fill="url(#bandFill)"/>
      <polygon points="0,0 28,0 0,28" fill="#6d6e71"/>
      <polygon points="530,138 530,166 502,166" fill="#6d6e71"/>
    </svg>
    <div class="contact-band__body">
      <p class="person">Daniel Marsh<span class="person__title">Managing Director</span></p>
      <p class="address">Suite 4, 112 Kerr Street, Leederville Western Australia 6007</p>
      <div class="contact-grid">
        <span class="contact-item">
          <svg viewBox="0 0 14 14" aria-hidden="true"><path d="M3 1h3l1 3-2 1a7 7 0 0 0 4 4l1-2 3 1v3c0 1-1 2-2 2A11 11 0 0 1 1 3c0-1 1-2 2-2z" fill="#fff"/></svg>
          08 9000 4815
        </span>
        <span class="contact-item">
          <svg viewBox="0 0 14 14" aria-hidden="true"><circle cx="7" cy="7" r="5.5" fill="none" stroke="#fff" stroke-width="1.5"/><circle cx="7" cy="7" r="2" fill="#fff"/></svg>
          d.marsh@klvapartners.com.au
        </span>
        <span class="contact-item">
          <svg viewBox="0 0 14 14" aria-hidden="true"><rect x="3.5" y="0.5" width="7" height="13" rx="1.2" fill="#fff"/><rect x="5" y="2.5" width="4" height="7" fill="#0d5aa7"/></svg>
          0400 731 562
        </span>
        <span class="contact-item">
          <svg viewBox="0 0 14 14" aria-hidden="true"><circle cx="7" cy="7" r="6" fill="none" stroke="#fff" stroke-width="1.3"/><path d="M1 7h12M7 1c-3 3-3 9 0 12M7 1c3 3 3 9 0 12" fill="none" stroke="#fff" stroke-width="1"/></svg>
          www.klvapartners.com.au
        </span>
      </div>
    </div>
  </div>
</section>

<section class="card card--back" aria-label="Business card back">
  <div class="back-panel"></div>
  <div class="corner corner--tl"></div>
  <div class="corner corner--br"></div>
  <div class="back-content">
    <p class="back-name"><span class="back-name__square"></span>KLVA Partners</p>
    <p class="tagline">Complete Workplace Risk &amp; Compliance Advisory Services</p>
    <p class="website">www.klvapartners.com.au</p>
  </div>
</section>

</body>
</html>
```